The Velvet Strands (Hair Extensions)

The Velvet Strands Are Hair Extension.
I would like the design to be very sleek, modern, and simple. (With a little Pop)
I currently have a lash company
www.TheVelvetBrow.example
So i want the boxes to kinda match the eyelash boxes. (But Not Red)
i definitely want the boxes to be White and Metallic Silver.

Industry/Entity Type

Hair And Beauty

Font styles to use
Script

Colors
5c5c5c
aaaaaa
606060
ffffff
000000

Requirements
Must have
• www.TheVelvetStrands.example
Nice to have
• (possibly with a slight neutral color design)

```html
<!DOCTYPE html>
<html lang="en">
<head>
<meta charset="utf-8">
<title>The Velvet Strands — Box Panel</title>
<link rel="stylesheet" href="https://fonts.googleapis.com/css2?family=Great+Vibes&family=Josefin+Sans:wght@300&display=swap">
<style>
  :root {
    --paper: #ffffff;
    --ink: #000000;
    --silver-dark: #5c5c5c;
    --silver-mid: #606060;
    --silver-light: #aaaaaa;
    --text-grey: #3a3a3a;
  }
  html, body {
    margin: 0;
    padding: 0;
    overflow: hidden;
    background: var(--paper);
  }
  .panel {
    position: relative;
    width: 1200px;
    height: 4220px;
    background: var(--paper);
    overflow: hidden;
    font-family: "Josefin Sans", sans-serif;
    font-weight: 300;
    color: var(--text-grey);
  }
  .flourish {
    position: absolute;
    display: block;
  }
  .flourish--top {
    left: 240px;
    top: 60px;
    width: 720px;
    height: 1210px;
  }
  .flourish--bottom {
    left: 270px;
    top: 2450px;
    width: 660px;
    height: 900px;
  }
  .brand {
    position: absolute;
    top: 1390px;
    left: 0;
    width: 1200px;
    text-align: center;
  }
  .brand__dot {
    display: block;
    width: 300px;
    height: 300px;
    margin: 0 auto 70px;
    border-radius: 50%;
    background: var(--ink);
  }
  .brand__name {
    margin: 0;
    font-family: "Great Vibes", cursive;
    font-weight: 400;
    font-size: 190px;
    line-height: 0.92;
    color: var(--ink);
  }
  .claim {
    position: absolute;
    left: 0;
    width: 1200px;
    margin: 0;
    text-align: center;
    font-weight: 300;
    line-height: 1;
  }
  .claim--percent {
    top: 3430px;
    font-size: 88px;
    color: var(--text-grey);
  }
  .claim--quality {
    top: 3615px;
    font-size: 38px;
    letter-spacing: 7px;
    color: var(--silver-mid);
  }
  .claim--origin {
    top: 3765px;
    font-size: 52px;
    letter-spacing: 6px;
    color: var(--text-grey);
  }
  .claim--web {
    top: 3960px;
    font-size: 38px;
    letter-spacing: 3px;
    color: var(--silver-dark);
  }
</style>
</head>
<body>
  <main class="panel">
    <svg class="flourish flourish--top" viewBox="0 0 720 1210" role="img" aria-label="Metallic silver interlaced scroll flourish ornament tapering upward like a tree">
      <defs>
        <linearGradient id="silverUp" x1="0" y1="0" x2="1" y2="1">
          <stop offset="0" stop-color="#ffffff"/>
          <stop offset="0.35" stop-color="#d6d6d6"/>
          <stop offset="0.6" stop-color="#aaaaaa"/>
          <stop offset="0.8" stop-color="#eeeeee"/>
          <stop offset="1" stop-color="#606060"/>
        </linearGradient>
      </defs>
      <path d="M360 0 C410 160 500 460 610 860 C690 1100 640 1200 360 1200 C80 1200 30 1100 110 860 C220 460 310 160 360 0 Z" fill="url(#silverUp)" opacity="0.75"/>
    </svg>

    <header class="brand">
      <span class="brand__dot" aria-hidden="true"></span>
      <h1 class="brand__name">The Velvet<br>Strands</h1>
    </header>

    <svg class="flourish flourish--bottom" viewBox="0 0 660 900" role="img" aria-label="Metallic silver interlaced scroll flourish ornament tapering downward">
      <defs>
        <linearGradient id="silverDown" x1="1" y1="0" x2="0" y2="1">
          <stop offset="0" stop-color="#606060"/>
          <stop offset="0.25" stop-color="#eeeeee"/>
          <stop offset="0.45" stop-color="#aaaaaa"/>
          <stop offset="0.7" stop-color="#d6d6d6"/>
          <stop offset="1" stop-color="#ffffff"/>
        </linearGradient>
      </defs>
      <path d="M330 0 C560 0 660 60 640 200 C620 420 450 680 330 900 C210 680 40 420 20 200 C0 60 100 0 330 0 Z" fill="url(#silverDown)" opacity="0.75"/>
    </svg>

    <p class="claim claim--percent">100%</p>
    <p class="claim claim--quality">PREMIUM VIRGIN HAIR</p>
    <p class="claim claim--origin">IMPORTED FROM INDIA</p>
    <p class="claim claim--web">www.TheVelvetStrands.example</p>
  </main>
</body>
</html>
```